VelloTask Business Card

Our company is called VelloTask and we are based in Tel Aviv, Israel. We create innovative and exciting methods for getting people on the web engaged with content. We need a cool yet professional business card that will represent our management level employees. keep in mind this is a start up company with a young atmosphere. You can be inspired by our logo (file attached, make sure you have the right font "Ubuntu-Condensed") Use the colors that are used in the logo and create a colourful and professional business card.

```html
<!DOCTYPE html>
<html lang="en">
<head>
<meta charset="utf-8">
<title>VelloTask Business Card</title>
<link href="https://fonts.googleapis.com/css2?family=Ubuntu+Condensed&family=Roboto+Condensed:wght@400&display=block" rel="stylesheet">
<style>
  :root {
    --bg-top: #e4e4e4;
    --bg-bottom: #b9b9b9;
    --paper: #f2f1ee;
    --ink: #1f1f1f;
    --brand-blue: #3aa9dc;
    --pink: #e6177f;
    --yellow: #f7d117;
    --green: #8cc63f;
    --blue: #3aa9dc;
    --purple: #8e2f8f;
    --orange: #f39a1e;
  }
  * { margin: 0; padding: 0; box-sizing: border-box; }
  html, body { width: 1200px; height: 850px; overflow: hidden; }
  body {
    background: linear-gradient(180deg, var(--bg-top), var(--bg-bottom));
    font-family: "Ubuntu Condensed", "Roboto Condensed", "Arial Narrow", sans-serif;
    color: var(--ink);
    position: relative;
  }
  .card {
    position: absolute;
    top: 215px;
    width: 420px;
    height: 420px;
    padding: 40px;
    box-shadow: 0 10px 24px rgba(0,0,0,0.22);
  }
  .card--back { left: 150px; }
  .card--front { left: 630px; }
  .card__border {
    position: absolute;
    inset: 0;
    background: linear-gradient(135deg,
      var(--yellow) 0%,
      var(--green) 22%,
      var(--blue) 42%,
      var(--purple) 62%,
      var(--pink) 80%,
      var(--orange) 100%);
  }
  .card__panel {
    width: 100%;
    height: 100%;
    background: var(--paper);
    position: relative;
  }
  .brand {
    display: flex;
    align-items: center;
    gap: 8px;
    font-weight: 400;
    white-space: nowrap;
  }
  .brand__dot {
    border-radius: 50%;
    background: var(--pink);
    flex: none;
  }
  .card--back .brand {
    position: absolute;
    top: 26px;
    right: 22px;
    font-size: 24px;
    color: var(--brand-blue);
  }
  .card--back .brand__dot { width: 14px; height: 14px; }
  .contact {
    position: absolute;
    left: 26px;
    top: 124px;
    font-size: 23px;
    line-height: 1.22;
  }
  .contact__role {
    font-size: 26px;
    margin-bottom: 10px;
  }
  .address {
    position: absolute;
    right: 22px;
    bottom: 24px;
    font-size: 17px;
    white-space: nowrap;
  }
  .card--front .card__panel {
    display: flex;
    align-items: center;
    justify-content: center;
  }
  .card--front .brand { font-size: 62px; gap: 14px; color: var(--ink); }
  .card--front .brand__dot { width: 30px; height: 30px; }
</style>
</head>
<body>
  <section class="card card--back" aria-label="Business card, contact side">
    <div class="card__border" role="img" aria-label="Colourful diagonal stripe border in yellow, green, blue, purple, pink and orange"></div>
    <div class="card__panel">
      <div class="brand"><span class="brand__dot"></span><span class="brand__name">VelloTask</span></div>
      <div class="contact">
        <p class="contact__role">Director</p>
        <p class="contact__phone">031-555-0192</p>
        <p class="contact__email">director@vellomail.com</p>
        <p class="contact__web">www.vellotask.com</p>
      </div>
      <p class="address">Street and number, Tel Aviv, Israel</p>
    </div>
  </section>

  <section class="card card--front" aria-label="Business card, brand side">
    <div class="card__border" role="img" aria-label="Colourful diagonal stripe border in yellow, green, blue, purple, pink and orange"></div>
    <div class="card__panel">
      <div class="brand"><span class="brand__dot"></span><span class="brand__name">VelloTask</span></div>
    </div>
  </section>
</body>
</html>
```